Business Card Design

It's an investment advisory service for individuals with all there investment needs. Also financial consulting to businesses and governmental agencies on retirement plans etc. It's personalized not commoditized help. Should show strength, knowledge and money orientation.
Updates

Reason: Will be out of town setting up office.

Reason: waiting for the 2/3rds of group to vote

Reason: only half the votes are in, I'm calling and getting verbals, but at this time we are down to 2 designs.

Industry/Entity Type

Investment

Contact Information for Business Card

B. Rel K. Financial Consulting and Wealth Management, Desmond Wick Harlow, 5172 Paseo Loma Verde Crest, San Diego, CA 92131-4817, Registered Investment Advisor

Requirements
Nice to have
• Something money oriented

```html
<!DOCTYPE html>
<html lang="en">
<head>
<meta charset="utf-8">
<title>B. Rel K. Financial Consulting and Wealth Management — Business Card</title>
<link rel="stylesheet" href="https://fonts.googleapis.com/css2?family=Ubuntu:wght@400;500;700&display=swap">
<style>
  :root {
    --page-bg: #d9d9d9;
    --card-white: #f4f4f2;
    --brand-blue: #08a0de;
    --text-gray: #6b6b6b;
    --text-white: #ffffff;
  }
  * { box-sizing: border-box; margin: 0; padding: 0; }
  html, body {
    width: 1200px; height: 1000px; overflow: hidden;
    background: var(--page-bg);
    font-family: "Ubuntu", sans-serif;
  }
  .canvas {
    width: 1200px; height: 1000px;
    display: flex; align-items: center; justify-content: center;
  }
  .business-card {
    width: 900px; height: 514px;
    display: flex;
    background: var(--card-white);
    box-shadow: 0 10px 30px rgba(0,0,0,0.18);
  }
  .brand-side {
    width: 46%;
    display: flex; flex-direction: column;
    align-items: center; justify-content: center;
    gap: 22px;
  }
  .brand-mark {
    display: flex; align-items: center; gap: 14px;
    color: var(--brand-blue);
  }
  .brand-mark .mark-circle {
    width: 58px; height: 58px; border-radius: 50%;
    background: var(--brand-blue);
  }
  .brand-mark .brand-name {
    font-size: 40px; font-weight: 500; letter-spacing: 0.5px;
  }
  .brand-tagline {
    color: var(--text-gray);
    font-size: 25px; font-weight: 400;
    text-align: right; line-height: 1.15;
  }
  .contact-side {
    width: 54%;
    background: var(--brand-blue);
    color: var(--text-white);
    padding: 92px 0 0 62px;
  }
  .person-name { font-size: 30px; font-weight: 700; letter-spacing: 0.3px; }
  .person-title { font-size: 17px; font-weight: 500; margin-top: 4px; letter-spacing: 0.3px; }
  .contact-icons { display: flex; gap: 14px; margin-top: 34px; }
  .contact-icon {
    width: 36px; height: 36px; border-radius: 50%;
    background: var(--text-white);
    display: flex; align-items: center; justify-content: center;
  }
  .contact-icon svg { width: 20px; height: 20px; fill: var(--brand-blue); }
  .address { margin-top: 22px; font-size: 22px; font-weight: 400; line-height: 1.3; letter-spacing: 0.3px; }
</style>
</head>
<body>
<main class="canvas">
  <article class="business-card">
    <section class="brand-side">
      <div class="brand-mark">
        <span class="mark-circle"></span>
        <span class="brand-name">B. Rel K.</span>
      </div>
      <p class="brand-tagline">Financial Consulting<br>and Wealth Management</p>
    </section>
    <section class="contact-side">
      <h1 class="person-name">Desmond Wick Harlow</h1>
      <p class="person-title">Investment Advisor</p>
      <div class="contact-icons">
        <span class="contact-icon" aria-label="Address">
          <svg viewBox="0 0 24 24"><path d="M12 3 2 12h3v8h5v-5h4v5h5v-8h3z"/></svg>
        </span>
        <span class="contact-icon" aria-label="Phone">
          <svg viewBox="0 0 24 24"><path d="M6.6 10.8a15.1 15.1 0 0 0 6.6 6.6l2.2-2.2c.3-.3.7-.4 1-.2 1.1.4 2.3.6 3.6.6.6 0 1 .4 1 1V20c0 .6-.4 1-1 1A17 17 0 0 1 3 4c0-.6.4-1 1-1h3.5c.6 0 1 .4 1 1 0 1.3.2 2.5.6 3.6.1.3 0 .7-.2 1z"/></svg>
        </span>
        <span class="contact-icon" aria-label="Email">
          <svg viewBox="0 0 24 24"><path d="M3 5h18v14H3zm2 2v.5l7 4.5 7-4.5V7l-7 4.5z"/></svg>
        </span>
      </div>
      <p class="address">5172 Paseo Loma Verde Crest<br>San Diego, CA 92131-4817</p>
    </section>
  </article>
</main>
</body>
</html>
```